BRIGHTWAY MOTOR DEALS
BRIGHTWAY MOTOR DEALS -
Creative Brief
Professional
DEAN VARLOW
SALES REP
742 N.CORVAL AVE HAMILTON OHIO 45019
BRIGHTWAYMOTORDEALS@QUILLMAIL.EXAMPLE
WWW.TORVENCARHOUSE.EXAMPLE

```html
<!DOCTYPE html>
<html lang="en">
<head>
<meta charset="utf-8">
<title>Brightway Motor Deals – Stationery</title>
<link href="https://fonts.googleapis.com/css2?family=Open+Sans:wght@400;700&display=swap" rel="stylesheet">
<style>
  :root{
    --bg-dark:#2e2e2e;
    --bg-light:#4a4a4a;
    --paper:#ffffff;
    --magenta:#b01f7c;
    --magenta-soft:#d86aa9;
    --green:#8cc63f;
    --green-soft:#c4e38f;
    --ink:#555555;
    --caption:#9a9a9a;
  }
  *{box-sizing:border-box;margin:0;padding:0}
  html,body{width:1200px;height:346px;overflow:hidden}
  body{
    position:relative;
    font-family:"Open Sans",Arial,sans-serif;
    background:radial-gradient(ellipse at 50% 40%,var(--bg-light),var(--bg-dark) 75%);
  }
  .sheet{position:absolute;background:var(--paper);box-shadow:0 2px 6px rgba(0,0,0,.45);overflow:hidden}
  .wave{position:absolute;left:0;bottom:0;width:100%}
  .brand{color:var(--magenta);font-weight:700;white-space:nowrap;text-align:center}
  .brand-mark{display:block;margin:0 auto 2px;border-radius:50%;background:var(--green)}
  .contact{color:var(--ink);white-space:nowrap}
  .caption{position:absolute;color:var(--caption);font-size:5px;text-align:center}

  /* business cards */
  .card-front{left:19px;top:82px;width:135px;height:76px}
  .card-front .brand{position:absolute;left:6px;top:6px;font-size:5px;text-align:left}
  .card-front .person{position:absolute;left:6px;top:22px;font-size:5.5px;font-weight:700;color:var(--magenta)}
  .card-front .role{position:absolute;left:6px;top:30px;font-size:4px;color:var(--ink)}
  .card-front .contact{position:absolute;left:50px;top:30px;font-size:2.9px;line-height:1.7}
  .card-back{left:19px;top:187px;width:135px;height:48px}
  .card-back .brand{position:absolute;left:0;right:0;top:12px;font-size:5.5px}

  /* letterheads */
  .letterhead{top:19px;width:231px;height:279px}
  .letterhead.first{left:163px}
  .letterhead.second{left:403px;width:226px}
  .letterhead .brand{position:absolute;left:30px;width:110px;top:8px;font-size:6px}
  .letterhead .contact{position:absolute;left:150px;top:9px;font-size:2.6px;line-height:1.7}
  .letterhead .footer{position:absolute;left:0;right:0;bottom:3px;font-size:3.4px;color:#fff;text-align:center}

  /* DL envelopes */
  .envelope{left:638px;width:255px}
  .envelope.front{top:62px;height:120px}
  .envelope.back{top:206px;height:125px}
  .envelope .brand{position:absolute;left:8px;top:8px;font-size:5.5px;text-align:center}
  .envelope .contact{position:absolute;left:8px;top:26px;font-size:2.8px;line-height:1.7}

  /* large envelopes */
  .dl{left:898px;width:254px}
  .dl.green{top:62px;height:96px}
  .dl.pink{top:126px;height:100px}
  .dl.open{top:200px;height:112px;background:#f4f4f4}
  .dl .brand{position:absolute;left:0;right:0;font-size:5.5px}
</style>
</head>
<body>

<!-- business card front -->
<div class="sheet card-front">
  <div class="brand"><span class="brand-mark" style="width:6px;height:6px;margin:0 0 2px"></span>BRIGHTWAY MOTOR DEALS</div>
  <div class="person">DEAN VARLOW</div>
  <div class="role">SALES REP</div>
  <div class="contact">
    (513) 555-0142<br>
    742 N.CORVAL AVE HAMILTON OHIO 45019<br>
    BRIGHTWAYMOTORDEALS@QUILLMAIL.EXAMPLE<br>
    WWW.TORVENCARHOUSE.EXAMPLE
  </div>
  <svg class="wave" viewBox="0 0 200 30" preserveAspectRatio="none" height="12">
    <path d="M0 14 C60 2 130 26 200 6 L200 30 L0 30Z" fill="var(--green)"/>
    <path d="M0 18 C60 8 130 30 200 10 L200 30 L0 30Z" fill="var(--magenta)"/>
  </svg>
</div>
<div class="caption" style="left:19px;top:160px;width:135px">Business Card Front</div>

<!-- business card back -->
<div class="sheet card-back">
  <div class="brand"><span class="brand-mark" style="width:7px;height:7px"></span>BRIGHTWAY MOTOR DEALS</div>
</div>
<div class="caption" style="left:19px;top:238px;width:135px">Business Card Back</div>

<!-- letterhead first page -->
<div class="sheet letterhead first">
  <div class="brand"><span class="brand-mark" style="width:10px;height:10px"></span>BRIGHTWAY MOTOR DEALS</div>
  <div class="contact">
    742 N.CORVAL AVE HAMILTON OHIO 45019<br>
    (513) 555-0142<br>
    BRIGHTWAYMOTORDEALS@QUILLMAIL.EXAMPLE
  </div>
  <svg class="wave" viewBox="0 0 200 40" preserveAspectRatio="none" height="22">
    <path d="M0 16 C50 4 140 30 200 8 L200 40 L0 40Z" fill="var(--green)"/>
    <path d="M0 22 C50 10 140 36 200 14 L200 40 L0 40Z" fill="var(--magenta)"/>
  </svg>
  <div class="footer">WWW.TORVENCARHOUSE.EXAMPLE</div>
</div>

<!-- letterhead second page -->
<div class="sheet letterhead second">
  <div class="brand"><span class="brand-mark" style="width:10px;height:10px"></span>BRIGHTWAY MOTOR DEALS</div>
  <svg class="wave" viewBox="0 0 200 40" preserveAspectRatio="none" height="22">
    <path d="M0 16 C50 4 140 30 200 8 L200 40 L0 40Z" fill="var(--green)"/>
    <path d="M0 22 C50 10 140 36 200 14 L200 40 L0 40Z" fill="var(--magenta)"/>
  </svg>
  <div class="footer">WWW.TORVENCARHOUSE.EXAMPLE</div>
</div>

<!-- DL envelope, plain -->
<div class="sheet envelope front">
  <div class="brand"><span class="brand-mark" style="width:7px;height:7px"></span>BRIGHTWAY MOTOR DEALS</div>
  <div class="contact">742 N.CORVAL AVE HAMILTON OHIO 45019<br>WWW.TORVENCARHOUSE.EXAMPLE</div>
</div>
<div class="caption" style="left:638px;top:184px;width:255px">DL Envelope Front</div>

<!-- DL envelope, with band -->
<div class="sheet envelope back">
  <div class="brand"><span class="brand-mark" style="width:7px;height:7px"></span>BRIGHTWAY MOTOR DEALS</div>
  <div class="contact">742 N.CORVAL AVE HAMILTON OHIO 45019<br>WWW.TORVENCARHOUSE.EXAMPLE</div>
  <svg class="wave" viewBox="0 0 200 30" preserveAspectRatio="none" height="18">
    <path d="M0 12 C60 2 140 26 200 6 L200 30 L0 30Z" fill="var(--green)"/>
    <path d="M0 16 C60 6 140 30 200 10 L200 30 L0 30Z" fill="var(--magenta)"/>
  </svg>
</div>
<div class="caption" style="left:638px;top:333px;width:255px">DL Envelope Back</div>

<!-- large envelope, green flap -->
<div class="sheet dl green">
  <svg style="position:absolute;left:0;top:0" width="254" height="56" viewBox="0 0 300 56" preserveAspectRatio="none">
    <path d="M0 0 H300 L150 54Z" fill="var(--green)"/>
    <path d="M0 0 L150 54 L300 0 L150 50Z" fill="var(--green-soft)"/>
  </svg>
  <div class="brand" style="top:12px;color:#2f2f2f">BRIGHTWAY MOTOR DEALS</div>
</div>

<!-- large envelope, magenta flap -->
<div class="sheet dl pink">
  <svg style="position:absolute;left:0;top:0" width="254" height="52" viewBox="0 0 300 52" preserveAspectRatio="none">
    <path d="M0 0 H300 L150 50Z" fill="var(--magenta)"/>
    <path d="M0 0 L150 50 L300 0 L150 46Z" fill="var(--magenta-soft)"/>
  </svg>
  <div class="brand" style="top:12px;color:#fff">BRIGHTWAY MOTOR DEALS</div>
</div>

<!-- large envelope, open -->
<div class="sheet dl open">
  <svg style="position:absolute;left:0;top:0" width="254" height="112" viewBox="0 0 300 112" preserveAspectRatio="none">
    <path d="M0 0 L150 62 L300 0" fill="none" stroke="#cfcfcf" stroke-width="1"/>
    <path d="M0 112 L130 52 M300 112 L170 52" fill="none" stroke="#d8d8d8" stroke-width="1"/>
  </svg>
</div>

</body>
</html>
```